New Business Card Design Project

Harbor of the Willow Wellness Clinic PLLC
Harborofthewillowwc.example
Board Certified Nursing Coach in life, health, & wellness.
Hypnotherapy, weight loss & vitamin supplement injections, IV hydration.
Offering mobile clinics

```html
<!DOCTYPE html>
<html lang="en">
<head>
<meta charset="utf-8">
<title>Harbor of the Willow Wellness Clinic – Business Card</title>
<link rel="stylesheet" href="https://fonts.googleapis.com/css2?family=Carlito:wght@400;700&display=swap">
<style>
  :root {
    --canvas: #acacac;
    --card-front: #fbfbf0;
    --card-back: #5e2f31;
    --ink-brown: #4b2f2f;
    --accent-orange: #d4532c;
    --accent-gold: #f2b03a;
    --cream: #fbf4e4;
    --white: #ffffff;
    --art-light: #9a6663;
    --art-dark: #5e2f31;
  }
  * { margin: 0; padding: 0; box-sizing: border-box; }
  html, body { width: 1200px; height: 1000px; overflow: hidden; }
  body {
    background: var(--canvas);
    font-family: "Carlito", "Calibri", sans-serif;
    position: relative;
  }
  .card {
    position: absolute;
    left: 293px;
    width: 615px;
    height: 354px;
    border-radius: 16px;
    overflow: hidden;
    box-shadow: 6px 8px 14px rgba(0,0,0,0.28);
  }
  .card-front { top: 133px; background: var(--card-front); color: var(--ink-brown); text-align: center; }
  .card-back { top: 526px; background: var(--card-back); }

  .wordmark { position: absolute; left: 0; right: 0; font-weight: 700; text-transform: uppercase; }
  .card-front .wordmark { top: 58px; color: var(--ink-brown); }
  .wordmark-name { display: block; font-size: 30px; letter-spacing: 2px; line-height: 32px; }
  .wordmark-sub { display: block; font-size: 15px; letter-spacing: 3px; line-height: 20px; margin-top: 6px; }

  .person-name { position: absolute; top: 160px; left: 0; right: 0; font-size: 25px; font-weight: 700; color: var(--accent-orange); }
  .person-title { position: absolute; top: 188px; left: 0; right: 0; font-size: 15px; letter-spacing: 4px; }
  .contact-icons { position: absolute; top: 219px; left: 0; right: 0; display: flex; justify-content: center; gap: 4px; }
  .contact-icons svg { width: 26px; height: 26px; }
  .contact-list { position: absolute; top: 255px; left: 0; right: 0; list-style: none; font-size: 19px; line-height: 24px; }

  .illustration-area {
    position: absolute; right: 0; top: 0; width: 330px; height: 354px;
    background: radial-gradient(circle at 55% 30%, var(--art-light) 0%, #7f4a49 35%, rgba(94,47,49,0) 75%);
  }
  .card-back .wordmark { top: 142px; left: 40px; width: 400px; text-align: center; color: var(--cream); }
  .card-back .wordmark-name { font-size: 32px; }
  .back-url { position: absolute; top: 222px; left: 40px; width: 400px; text-align: center; font-size: 21px; font-weight: 700; color: var(--accent-gold); }
  .services { position: absolute; top: 258px; left: 0; width: 478px; text-align: center; font-size: 13px; line-height: 17px; color: var(--white); }
</style>
</head>
<body>
  <section class="card card-front">
    <div class="wordmark">
      <span class="wordmark-name">Harbor of the Willow</span>
      <span class="wordmark-sub">Wellness Clinic</span>
    </div>
    <div class="person-name">NAME SURNAME</div>
    <div class="person-title">TITLE</div>
    <div class="contact-icons">
      <svg viewBox="0 0 26 26" aria-label="Phone"><circle cx="13" cy="13" r="13" fill="var(--accent-gold)"/><path d="M9 7c1 0 2 2 2 3s-1 1-1 2 3 4 4 4 1-1 2-1 3 1 3 2-1 2-2 2C12 19 7 14 7 9c0-1 1-2 2-2z" fill="#fff"/></svg>
      <svg viewBox="0 0 26 26" aria-label="Email"><circle cx="13" cy="13" r="13" fill="var(--accent-gold)"/><rect x="7" y="9" width="12" height="8" fill="#fff"/><path d="M7 9l6 5 6-5" fill="none" stroke="var(--accent-gold)" stroke-width="1"/></svg>
      <svg viewBox="0 0 26 26" aria-label="Website"><circle cx="13" cy="13" r="13" fill="var(--accent-gold)"/><g fill="none" stroke="#fff" stroke-width="1.2"><circle cx="13" cy="13" r="6"/><ellipse cx="13" cy="13" rx="2.5" ry="6"/><path d="M7 13h12M8 10h10M8 16h10"/></g></svg>
    </div>
    <ul class="contact-list">
      <li>(012) 555-0148</li>
      <li>name@harborofthewillowwc.example</li>
      <li>harborofthewillowwc.example</li>
    </ul>
  </section>

  <section class="card card-back">
    <div class="illustration-area" role="img" aria-label="Large tonal emblem illustration in muted rose tones"></div>
    <div class="wordmark">
      <span class="wordmark-name">Harbor of the Willow</span>
      <span class="wordmark-sub">Wellness Clinic</span>
    </div>
    <div class="back-url">harborofthewillowwc.example</div>
    <p class="services">
      Board Certified Nursing Coach in life, health, &amp; wellness.<br>
      Hypnotherapy, weight loss &amp; vitamin supplement injections, IV hydration.<br>
      Offering mobile clinics
    </p>
  </section>
</body>
</html>
```